VARSEK MOBILE APP RE-DESIGN - MINIMALISTIC AND CLEAN DESIGN

We are looking for a design that is minimalistic, clean, modern and appealing to millennials...
IMPORTANT: This is NOT a logo design nor a website design... This is for a mobile App Design. You can download our app on iOS or Android: "VARSEK eLINKUP"

We are attaching our new logo and some apps that we like the design, colors, shadows, 3d effects, style, etc...

For content, you can check our website: www.varsek-app.example

Please feel free to ask questions, it's very important that you understand the project. Thank you

Also, check out this website...we do like the design and colors: https://brontil-demo.example/
Updates

This is not for a logo design... this is for a mobile app design.... please download our app on iOS: VARSEK eLINKUP... THANK YOU

Target Market(s)

20 - 35
60% Male 40 Female

Requirements
Must have
• great graphics, color shadows for 3d effects, great colors with transparency, IMPORTANT: CLEAN DESIGN, Minimalistic.

```html
<!DOCTYPE html>
<html lang="en">
<head>
<meta charset="utf-8">
<title>Varsek — Splash Screen</title>
<link rel="stylesheet" href="https://fonts.googleapis.com/css2?family=Ubuntu:wght@500&family=Roboto:wght@400&display=swap">
<style>
  :root {
    --page-bg: #3f63b8;
    --screen-top: #2e248e;
    --screen-mid: #1f5bb5;
    --screen-bottom: #00c8fa;
    --text-light: #ffffff;
    --mark-fill: #1ea4e6;
  }
  * { margin: 0; padding: 0; box-sizing: border-box; }
  html, body {
    width: 1200px;
    height: 1200px;
    overflow: hidden;
    background: var(--page-bg);
  }
  .canvas {
    position: relative;
    width: 1200px;
    height: 1200px;
    display: flex;
    align-items: center;
    justify-content: center;
  }
  .splash-screen {
    position: relative;
    width: 517px;
    height: 1120px;
    border-radius: 44px;
    overflow: hidden;
    background: linear-gradient(160deg,
      var(--screen-top) 0%,
      var(--screen-top) 30%,
      var(--screen-mid) 58%,
      var(--screen-bottom) 100%);
  }
  .brand {
    position: absolute;
    top: 258px;
    left: 0;
    right: 0;
    display: flex;
    align-items: center;
    justify-content: center;
    gap: 14px;
  }
  .brand-dot {
    width: 38px;
    height: 38px;
    border-radius: 50%;
    background: var(--mark-fill);
  }
  .brand-name {
    font-family: "Ubuntu", sans-serif;
    font-weight: 500;
    font-size: 48px;
    letter-spacing: 0.5px;
    color: var(--text-light);
    line-height: 1;
  }
  .app-version {
    position: absolute;
    top: 1060px;
    left: 0;
    right: 0;
    text-align: center;
    font-family: "Roboto", sans-serif;
    font-weight: 400;
    font-size: 19px;
    letter-spacing: 0.5px;
    color: var(--text-light);
  }
</style>
</head>
<body>
  <main class="canvas">
    <section class="splash-screen" aria-label="Varsek app splash screen">
      <div class="brand">
        <span class="brand-dot" aria-hidden="true"></span>
        <span class="brand-name">varsek</span>
      </div>
      <p class="app-version">v 0.1.0</p>
    </section>
  </main>
</body>
</html>
```